New Alcoholic Spiked Seltzer Line

We need a can design for a line of low calorie alcoholic seltzer. This product is a sparkling water and vodka drink with no sugar added in a slim 12 oz can.

This is a lighter, healthier, alternative to the sugary ready-to-drinks on the market. The product contains only 3 ingredients: Vodka, Water and Natural Flavors. It has only 100 calories but still has 5% alcohol, so you don't need to sacrifice alcohol to cut calories.

This product also does not contain any preservatives.

We want this design to communicate the following objectives to the consumer and in this order:

1. Appetizing product
2.Low calorie
3.Communicate the type of beverage (Spiked Seltzer)

The brand name of the product is VELKA.

The flavor of the product needed to be used for the design is Mango-Orange.

Comparable products are:

www.brisavelfizz.example/
https://www.tarnowbubble.example
https://quellrind.example/

The designs should not infringe or copy the creative directions of the products mentionned above. They are only given so that you can better understand the type of product we are developing.

Target Market(s)

Young Professional women between the ages of 25 and 44

Industry/Entity Type

Product

Colors

Designer to choose colors to be used in the design.

Requirements
Must have
• Design extendibility, meaning it can be adapted for other flavors.
• This is a new category in the market we are targeting, so consumers must easily be able to identify what type of product this is.

```html
<!DOCTYPE html>
<html lang="en">
<head>
<meta charset="utf-8">
<title>VELKA Spiked Seltzer – Mango-Orange Can Label</title>
<link rel="stylesheet" href="https://fonts.googleapis.com/css2?family=Comfortaa:wght@400;700&family=PT+Sans:wght@400;700&display=swap">
<style>
  :root {
    --silver-light: #f3f4f5;
    --silver-mid: #dcdee0;
    --silver-dark: #b9bcbf;
    --ink: #1a1a1a;
    --brand-red: #d71f27;
    --mango: #f5961f;
    --mango-mid: #e0861c;
    --mango-deep: #b5651a;
    --art-dark: #151515;
    --art-red: #c8141c;
    --art-pale: #eceded;
  }
  html, body {
    margin: 0;
    padding: 0;
    width: 1200px;
    height: 2546px;
    overflow: hidden;
  }
  .label {
    position: relative;
    width: 1200px;
    height: 2546px;
    overflow: hidden;
    background: linear-gradient(90deg, var(--silver-dark) 0%, var(--silver-mid) 12%, var(--silver-light) 30%, var(--silver-mid) 52%, var(--silver-light) 72%, var(--silver-mid) 88%, var(--silver-dark) 100%);
    font-family: "PT Sans", sans-serif;
    color: var(--ink);
  }
  .mascot-art {
    position: absolute;
    left: 135px;
    top: 627px;
    width: 930px;
    height: 680px;
    background:
      radial-gradient(ellipse 22% 42% at 50% 58%, var(--art-pale) 0%, var(--art-pale) 55%, rgba(236,237,237,0) 100%),
      radial-gradient(ellipse 50% 50% at 50% 50%, rgba(21,21,21,0.85) 0%, rgba(200,20,28,0.75) 45%, rgba(200,20,28,0.35) 75%, rgba(200,20,28,0) 100%);
  }
  .wordmark {
    position: absolute;
    left: 0;
    top: 1320px;
    width: 1200px;
    margin: 0;
    text-align: center;
    font-family: "Comfortaa", sans-serif;
    font-weight: 700;
    font-size: 260px;
    line-height: 1;
    letter-spacing: 6px;
    color: var(--ink);
  }
  .category {
    position: absolute;
    left: 0;
    top: 1640px;
    width: 1200px;
    margin: 0;
    text-align: center;
    font-family: "Comfortaa", sans-serif;
    font-weight: 400;
    font-size: 76px;
    line-height: 1;
    letter-spacing: 3px;
    color: var(--ink);
  }
  .tagline {
    position: absolute;
    left: 0;
    top: 1756px;
    width: 1200px;
    margin: 0;
    text-align: center;
    font-family: "Comfortaa", sans-serif;
    font-weight: 400;
    font-size: 44px;
    line-height: 1;
    letter-spacing: 2px;
    color: var(--brand-red);
  }
  .flavor-band {
    position: absolute;
    left: 135px;
    top: 1947px;
    width: 930px;
    height: 187px;
    background: linear-gradient(90deg, var(--mango) 0%, var(--mango-mid) 50%, var(--mango-deep) 100%);
    display: flex;
    align-items: center;
    justify-content: center;
  }
  .flavor-name {
    font-family: "PT Sans", sans-serif;
    font-weight: 400;
    font-size: 68px;
    letter-spacing: 1px;
    color: var(--ink);
  }
  .ingredients {
    position: absolute;
    left: 0;
    top: 2162px;
    width: 1200px;
    margin: 0;
    text-align: center;
    font-size: 52px;
    line-height: 1.2;
  }
  .nutrition {
    position: absolute;
    left: 0;
    top: 2238px;
    width: 1200px;
    margin: 0;
    text-align: center;
    font-size: 50px;
    font-weight: 700;
    line-height: 1.2;
  }
</style>
</head>
<body>
  <main class="label">
    <div class="mascot-art" role="img" aria-label="Illustration of a ram's head with large curled black and red horns"></div>
    <h1 class="wordmark">VELKA</h1>
    <p class="category">spiked seltzer</p>
    <p class="tagline">low calorie alcoholic seltzer</p>
    <div class="flavor-band"><span class="flavor-name">MANGO-ORANGE</span></div>
    <p class="ingredients">Vodka, Water and Natural Flavors</p>
    <p class="nutrition">5% alcohol - 100 calories</p>
  </main>
</body>
</html>
```